Building company with a modern and unique product looking for a business card to help us stand out

We currently have a logo but as our business has grown, we feel that our business card is not reflecting our modern and high quality product and help us stand out from the crowd. Our business is mainly in the construction of new homes using a unique method and materials that makes our homes fire proof, vermin and pest resistant and rated to the maximum cyclone category (category 5). We need a business card that helps us stand out as well as communicating professionalism, high quality and trustworthiness. I have attached our current logo with a black and white option, as well as our business card which is double sided. We would like to retain as much of the information that is currently on our business cards, but presented in a more sleek way. We do like our current colour palette ( white, black, yellow and grey) and have been looking primarily at business cards with a black background however we are open to other combinations of colour and layout as long as we stand out. Please feel free to tweak our logo to make it more suitable for a business card, we like the black option that we use but we have had trouble trying to get the white area to match the rest of the logo and blend effectively into a business card. Please do not hesitate to contact us with any questions as we really want this to be successful!

Target Market(s)

Large contracts including government and larger companies

Industry/Entity Type

Business

Contact Information for Business Card

We will be providing this business card to potential clients including key government ministers and large funding companies, our business card should show that we are professional and reliable.

Requirements
Must have
• It must be easy to read and pleasing to the eye, It must contain as much of the information on the current business card and unless something really stands out, we will most likely pick a design that has all of the information included. It must include our logo of course and have some colour included.
Nice to have
• We are looking for a high end business card and would like to see designs that reflect this. We like the gloss/matte contrast, plastic cards with opaque/coloured areas and unique features not seen on everyday paper business cards. It would be nice to see a few different colour combinations, we are open to new ideas so please feel free to take some artistic licence.
Should not have
• Must not be too busy, difficult to read or be distracting from the information conveyed. Other than this please feel free to add your own touches and make it unique!

```html
<!DOCTYPE html>
<html lang="en">
<head>
<meta charset="utf-8">
<title>Ardent Building Company – Business Card</title>
<link rel="stylesheet" href="https://fonts.googleapis.com/css2?family=Open+Sans:wght@400;600;700&display=swap">
<style>
  :root {
    --ink: #0b0b0b;
    --paper: #ffffff;
    --gold: #d4ad3c;
    --gold-deep: #b8902a;
    --grey: #9a9a9a;
    --grey-light: #cfcfcf;
    --stage: #ececec;
  }
  * { box-sizing: border-box; margin: 0; padding: 0; }
  html, body {
    width: 1200px; height: 913px; overflow: hidden;
    background: var(--stage);
    font-family: "Open Sans", Arial, sans-serif;
  }
  .card {
    position: absolute; top: 301px;
    width: 540px; height: 310px;
    border-radius: 16px; overflow: hidden;
    box-shadow: 0 6px 18px rgba(0,0,0,.18);
  }
  .card--front { left: 45px; background: var(--paper); }
  .card--back { left: 615px; background: var(--ink); }
  .card__art { position: absolute; inset: 0; }

  .brand { position: absolute; display: flex; align-items: center; gap: 10px; }
  .brand__mark { width: 16px; height: 16px; background: var(--gold); flex: none; }
  .brand__name { font-weight: 600; font-size: 22px; line-height: 1.15; }
  .card--front .brand { left: 34px; top: 128px; }
  .card--front .brand__name { color: var(--gold-deep); width: 190px; }
  .card--back .brand { left: 150px; top: 70px; }
  .card--back .brand__mark { background: var(--paper); }
  .card--back .brand__name { color: var(--paper); width: 240px; }

  .contact {
    position: absolute; right: 24px; top: 74px;
    color: var(--paper); text-align: right;
  }
  .contact__name { font-weight: 700; font-size: 22px; }
  .contact__role { color: var(--gold); font-size: 13px; font-weight: 600; margin-top: 2px; }
  .contact__abn { font-size: 12px; margin-top: 3px; }
  .contact__list { list-style: none; margin-top: 16px; font-size: 13px; line-height: 1.6; }
  .contact__list li { display: flex; justify-content: flex-end; align-items: center; gap: 8px; }
  .contact__icon { width: 12px; height: 12px; fill: var(--gold); flex: none; }

  .features {
    position: absolute; left: 150px; top: 170px;
    list-style: none; color: var(--paper);
    font-size: 14px; line-height: 1.45;
  }
  .features li { display: flex; align-items: center; gap: 10px; }
  .features li::before {
    content: ""; width: 10px; height: 10px; border-radius: 50%;
    background: var(--gold); flex: none;
  }
</style>
</head>
<body>

<section class="card card--front" aria-label="Card front">
  <svg class="card__art" viewBox="0 0 540 310" aria-hidden="true">
    <path d="M330,0 C300,60 286,110 278,170 C270,230 250,280 214,310" fill="none" stroke="var(--grey-light)" stroke-width="6"/>
    <path d="M346,0 C314,60 298,110 290,170 C282,230 262,280 228,310" fill="none" stroke="var(--gold)" stroke-width="9"/>
    <path d="M362,0 C328,60 312,110 304,170 C296,230 276,280 244,310 L540,310 L540,0 Z" fill="var(--ink)"/>
  </svg>

  <div class="brand">
    <span class="brand__mark"></span>
    <span class="brand__name">Ardent Building Company</span>
  </div>

  <div class="contact">
    <p class="contact__name">Marcus Ellery</p>
    <p class="contact__role">Managing Director</p>
    <p class="contact__abn">ABN: 12 345 678 901</p>
    <ul class="contact__list">
      <li>0400 123 456
        <svg class="contact__icon" viewBox="0 0 12 12"><path d="M2 1h3l1 3-2 1a7 7 0 0 0 3 3l1-2 3 1v3c-6 0-10-4-10-10z"/></svg></li>
      <li>(02) 5550 1234
        <svg class="contact__icon" viewBox="0 0 12 12"><path d="M1 4c0-2 10-2 10 0v1H8V4H4v1H1zM3 6h6l1 5H2z"/></svg></li>
      <li>hello@ardentbuild.com
        <svg class="contact__icon" viewBox="0 0 12 12"><path d="M1 2h10v8H1zM2 3v.5l4 3 4-3V3z" fill-rule="evenodd"/></svg></li>
    </ul>
  </div>
</section>

<section class="card card--back" aria-label="Card back">
  <div class="brand">
    <span class="brand__mark"></span>
    <span class="brand__name">Ardent Building Company</span>
  </div>
  <ul class="features">
    <li>Specialising in</li>
    <li>Homes that are</li>
    <li>Fire Proof</li>
    <li>Climate Proof</li>
    <li>Cyclone Rated (Cat. 5)</li>
  </ul>
</section>

</body>
</html>
```